Wrap needed for mobile fleet washing service

We need a wrap design for the mobile fleet washing division of our company, Brisq. We send crews of guys to our customers' locations to wash their fleet vehicles with pressure washers and chemicals, so they don't have to wash their vehicles themselves. We wash dump trucks, tractor-trailers, and garbage trucks, primarily. The wrap needs to fit a 2017 Dolvo cabover truck with an 18 foot box on it. Wrap needs to be clean, modern, and professional.
Target Market(s)
Businesses with fleets-- hauling companies, garbage companies, trucking companies.
Industry/Entity Type
Service, Transportation

```html
<!DOCTYPE html>
<html lang="en">
<head>
<meta charset="utf-8">
<title>Brisq Fleet Washing – Truck Wrap</title>
<link href="https://fonts.googleapis.com/css2?family=Montserrat:ital,wght@0,600;0,700;1,800&display=swap" rel="stylesheet">
<style>
  :root {
    --bg: #eef1f4;
    --blue-deep: #0a2fa8;
    --blue-main: #1450d6;
    --blue-bright: #1e8ff0;
    --cyan-glow: #5fd8ff;
    --illustration-a: #8fd3ff;
    --illustration-b: #2f6fd8;
    --white: #ffffff;
    --cab-blue: #1f62d4;
  }
  * { margin: 0; padding: 0; box-sizing: border-box; }
  html, body { width: 1200px; height: 900px; overflow: hidden; background: var(--bg); }
  body { position: relative; font-family: "Montserrat", sans-serif; color: var(--white); }

  .box-panel {
    position: absolute; left: 40px; top: 110px; width: 1120px; height: 452px;
    background:
      radial-gradient(circle at 44% 42%, rgba(190,245,255,.95) 0, rgba(95,216,255,.55) 9%, rgba(30,143,240,0) 34%),
      linear-gradient(100deg, var(--blue-main) 0%, var(--blue-bright) 40%, var(--blue-main) 62%, var(--blue-deep) 100%);
    overflow: hidden;
  }
  .bubble { position: absolute; border-radius: 50%;
    background: radial-gradient(circle at 35% 30%, rgba(255,255,255,.7), rgba(95,216,255,.35) 45%, rgba(30,143,240,.15));
  }
  .brand-name {
    position: absolute; left: 26px; top: 24px;
    font-weight: 600; font-size: 236px; line-height: 1; letter-spacing: -4px;
  }
  .service-line {
    position: absolute; left: 124px; top: 285px;
    font-weight: 700; font-size: 54px; letter-spacing: 1px;
  }
  .contact-row {
    position: absolute; left: 36px; top: 372px; width: 680px;
    display: flex; align-items: center; gap: 12px; white-space: nowrap;
    font-weight: 800; font-style: italic; font-size: 32px; letter-spacing: 1px;
  }
  .contact-icon { width: 36px; height: 36px; flex: none; }
  .contact-row .gap { width: 10px; }

  .mascot-art {
    position: absolute; right: 0; top: 0; width: 390px; height: 452px;
    background:
      radial-gradient(ellipse at 50% 58%, var(--illustration-a) 0, #56a8f0 38%, var(--illustration-b) 62%, rgba(47,111,216,0) 78%),
      linear-gradient(180deg, #2c55c4, #1b3fb4);
  }

  .cab-panel {
    position: absolute; left: 700px; top: 612px; width: 460px; height: 240px;
    border-radius: 120px 18px 18px 18px;
    background: radial-gradient(circle at 30% 40%, var(--blue-bright), var(--cab-blue) 55%, var(--blue-deep));
    overflow: hidden;
  }
  .cab-lockup { position: absolute; left: 70px; top: 96px; display: flex; align-items: center; gap: 18px; }
  .cab-brand { font-weight: 600; font-size: 58px; line-height: 1; }
  .cab-divider { width: 3px; height: 62px; background: var(--white); }
  .cab-service { font-weight: 700; font-size: 20px; line-height: 1.35; letter-spacing: .5px; }
</style>
</head>
<body>
  <section class="box-panel" aria-label="Box side wrap">
    <span class="bubble" style="left:470px;top:60px;width:70px;height:70px"></span>
    <span class="bubble" style="left:520px;top:40px;width:34px;height:34px"></span>
    <span class="bubble" style="left:600px;top:60px;width:100px;height:100px"></span>
    <span class="bubble" style="left:560px;top:5px;width:46px;height:46px"></span>

    <div class="brand-name">Brisq</div>
    <div class="service-line">FLEET WASHING</div>

    <div class="contact-row">
      <svg class="contact-icon" viewBox="0 0 40 40" aria-hidden="true">
        <circle cx="20" cy="20" r="17" fill="none" stroke="#fff" stroke-width="3"/>
        <path d="M13 11c1-1 3-1 4 1l2 3c.6 1 .3 2-.5 2.7l-1.2 1c1 2.4 2.6 4 5 5l1-1.2c.7-.8 1.8-1 2.7-.5l3 2c1.3 1 1.3 3 .2 4-2 2-5 2.4-8 .6-3.6-2-6.4-5-8.3-8.7-1.6-3-1.2-5.9.1-7.9z" fill="#fff"/>
      </svg>
      <span>5550142737</span>
      <span class="gap"></span>
      <svg class="contact-icon" viewBox="0 0 40 40" aria-hidden="true">
        <circle cx="20" cy="20" r="17" fill="none" stroke="#fff" stroke-width="3"/>
        <rect x="12.5" y="12" width="15" height="11" rx="1.5" fill="none" stroke="#fff" stroke-width="2.4"/>
        <rect x="10" y="25" width="20" height="3" rx="1.2" fill="#fff"/>
      </svg>
      <span>brisqwash.com</span>
    </div>

    <div class="mascot-art" role="img" aria-label="Illustration of a smiling washer in a cap scrubbing a foamy blue car amid water splashes and bubbles"></div>
  </section>

  <section class="cab-panel" aria-label="Cab door wrap">
    <span class="bubble" style="left:330px;top:170px;width:56px;height:56px"></span>
    <span class="bubble" style="left:380px;top:150px;width:46px;height:46px"></span>
    <div class="cab-lockup">
      <span class="cab-brand">Brisq</span>
      <span class="cab-divider"></span>
      <span class="cab-service">FLEET<br>WASHING</span>
    </div>
  </section>
</body>
</html>
```